Used Car Dealer seeks an Amazing Business Card Design

We are looking for a business card design that incorporates our logo and grabs the attention of anyone we give the business card to.

Looking to use the same colors as the logo. Our Logo choice is the black background with Red and Silver/Grey Lettering.

We also would like to see some embossed designs.

Target Market(s)

Used Car Buyers, Automotive, Auto

Industry/Entity Type

Automotive

Contact Information for Business Card

BVEL7K
Gordon Whitlock
482 Tarrow Lane
Suite 207
Ashvale, NR 10482
Office (010) 555-0142
Cell (010) 555-0187
bvel7kga@quellmail.com
www.bvel7kga.com

Colors
ffffff
ee3036

Requirements
Must have
• Must include our logo (Black Background with Red and Silver/Grey Lettering)
Nice to have
• Embossed Design. Can be Single or Double Sided.

```html
<!DOCTYPE html>
<html lang="en">
<head>
<meta charset="utf-8">
<title>BVEL7K Business Card</title>
<link rel="stylesheet" href="https://fonts.googleapis.com/css2?family=Open+Sans:wght@400;700&display=swap">
<style>
  :root {
    --ink: #050505;
    --paper: #ffffff;
    --red: #ee3036;
    --silver: #c9cbcf;
    --stripe-grey: #a9a9ab;
    --stripe-lilac: #e6e4f2;
    --text-dark: #3a3a3a;
    --backdrop: #e9e9ea;
  }
  * { box-sizing: border-box; margin: 0; padding: 0; }
  html, body {
    width: 1200px; height: 1000px; overflow: hidden;
    background: var(--backdrop);
    font-family: "Open Sans", Arial, sans-serif;
  }
  .canvas {
    width: 1200px; height: 1000px;
    display: flex; flex-direction: column;
    align-items: center; justify-content: center; gap: 40px;
  }
  .card {
    width: 770px; height: 440px;
    display: flex; flex-direction: column;
    background: var(--ink);
    box-shadow: 0 6px 18px rgba(0,0,0,.18);
    overflow: hidden;
  }
  .card__dark { flex: 1; position: relative; }
  .card__contact {
    height: 132px; background: var(--paper);
    display: flex; align-items: flex-start;
    padding: 32px 48px 0; gap: 46px;
  }
  .stripe--grey { height: 7px; background: var(--stripe-grey); }
  .stripe--lilac { height: 7px; background: var(--stripe-lilac); }
  .stripe--red { height: 42px; background: var(--red); }

  .wordmark {
    display: flex; align-items: center; gap: 12px;
    color: var(--silver); font-weight: 700;
    letter-spacing: 1px; white-space: nowrap;
  }
  .wordmark__dot { border-radius: 50%; background: var(--red); flex: none; }
  .card--front .wordmark {
    position: absolute; left: 60px; top: 82px; font-size: 50px;
  }
  .card--front .wordmark__dot { width: 18px; height: 18px; }
  .holder-name {
    position: absolute; right: 100px; bottom: 50px;
    color: var(--paper); font-weight: 700; font-size: 24px;
    letter-spacing: 0.5px; text-transform: uppercase; white-space: nowrap;
  }
  .contact-item {
    display: flex; align-items: flex-start; gap: 10px;
    color: var(--text-dark); font-size: 15px; line-height: 1.45;
    white-space: nowrap;
  }
  .contact-item address { font-style: normal; }
  .contact-item svg { flex: none; margin-top: 3px; }

  .card--back .card__dark {
    display: flex; align-items: center; justify-content: center;
  }
  .card--back .wordmark { font-size: 64px; }
  .card--back .wordmark__dot { width: 22px; height: 22px; }
  .card--back .stripe--lilac { height: 10px; }
  .card--back .stripe--red { height: 44px; }
</style>
</head>
<body>
<main class="canvas">
  <section class="card card--front" aria-label="Business card front">
    <div class="card__dark">
      <div class="wordmark"><span class="wordmark__dot"></span><span>BVEL7K</span></div>
      <p class="holder-name">Gordon Whitlock</p>
    </div>
    <div class="card__contact">
      <div class="contact-item">
        <svg width="16" height="20" viewBox="0 0 16 20" aria-hidden="true">
          <path d="M8 0C3.6 0 0 3.4 0 7.6 0 13 8 20 8 20s8-7 8-12.4C16 3.4 12.4 0 8 0z" fill="var(--red)"/>
          <circle cx="8" cy="7.5" r="3" fill="var(--paper)"/>
        </svg>
        <address>482 Tarrow Lane<br>Suite 207<br>Ashvale, NR 10482</address>
      </div>
      <div class="contact-item">
        <svg width="18" height="18" viewBox="0 0 24 24" aria-hidden="true">
          <path d="M6.6 10.8c1.4 2.8 3.8 5.1 6.6 6.6l2.2-2.2c.3-.3.7-.4 1-.2 1.1.4 2.3.6 3.6.6.6 0 1 .4 1 1V20c0 .6-.4 1-1 1C10.6 21 3 13.4 3 4c0-.6.4-1 1-1h3.5c.6 0 1 .4 1 1 0 1.3.2 2.5.6 3.6.1.3 0 .7-.2 1z" fill="var(--red)"/>
        </svg>
        <p>(010) 555-0142<br>(010) 555-0187</p>
      </div>
      <div class="contact-item">
        <svg width="18" height="18" viewBox="0 0 24 24" aria-hidden="true">
          <circle cx="12" cy="12" r="11" fill="var(--red)"/>
          <g fill="none" stroke="var(--paper)" stroke-width="1.5">
            <circle cx="12" cy="12" r="8"/>
            <ellipse cx="12" cy="12" rx="3.5" ry="8"/>
            <path d="M4 12h16M5.5 8h13M5.5 16h13"/>
          </g>
        </svg>
        <p>bvel7kga@quellmail.com<br>www.bvel7kga.com</p>
      </div>
    </div>
    <div class="stripe--grey"></div>
    <div class="stripe--lilac"></div>
    <div class="stripe--red"></div>
  </section>

  <section class="card card--back" aria-label="Business card back">
    <div class="card__dark">
      <div class="wordmark"><span class="wordmark__dot"></span><span>BVEL7K</span></div>
    </div>
    <div class="stripe--lilac"></div>
    <div class="stripe--red"></div>
  </section>
</main>
</body>
</html>
```